PENNIMARTEL & PENNIMARTEL,LLP NEEDS A NEW LETTERHEAD DESIGN

a conservative yet contemporary layout befitting a long established
firm, consistent with the times, some form of logo so it catches ones attention, and is
admirable, but portrays integrity
Updates

I would like to approve #22066987 Please advise how to do this as it’s confusing on the site so I can approve payment for the designer

Target Market(s)

real estate investors and building management people

Industry/Entity Type

Law Firm

Font styles to use
Serif

Colors

Designer to choose colors to be used in the design.

Requirements
Must have
• some form of conservative logo

```html
<!DOCTYPE html>
<html lang="en">
<head>
<meta charset="utf-8">
<title>Pennimartel &amp; Pennimartel, LLP — Letterhead</title>
<link rel="stylesheet" href="https://fonts.googleapis.com/css2?family=Roboto:wght@400;500&display=swap">
<style>
  :root {
    --backdrop: #cdcdcd;
    --paper: #fbfbfb;
    --brand-blue: #22528a;
    --brand-grey: #6b6b6e;
    --text-grey: #6f6f73;
    --white: #ffffff;
  }
  html, body {
    margin: 0;
    padding: 0;
    width: 1200px;
    height: 922px;
    overflow: hidden;
    background: var(--backdrop);
    font-family: "Roboto", Arial, sans-serif;
  }
  .letterhead {
    position: absolute;
    left: 268px;
    top: 31px;
    width: 664px;
    height: 860px;
    background: var(--paper);
    box-shadow: 0 12px 30px rgba(0, 0, 0, 0.12);
  }
  .brand {
    position: absolute;
    left: 52px;
    top: 52px;
    display: flex;
    align-items: center;
    gap: 12px;
  }
  .brand-square {
    width: 30px;
    height: 30px;
    background: var(--brand-blue);
  }
  .brand-name {
    margin: 0;
    color: var(--brand-blue);
    font-weight: 500;
    font-size: 15px;
    line-height: 1.25;
    letter-spacing: 0.12em;
    text-transform: uppercase;
  }
  .contact {
    position: absolute;
    top: 64px;
    right: 44px;
    display: flex;
    gap: 18px;
    font-size: 9.5px;
    line-height: 1.35;
    color: var(--text-grey);
  }
  .contact address {
    font-style: normal;
  }
  .contact .firm {
    color: var(--brand-blue);
    font-weight: 500;
  }
  .contact-lines {
    list-style: none;
    margin: 10px 0 0;
    padding: 0;
  }
  .contact-lines li {
    display: flex;
    align-items: center;
    gap: 4px;
  }
  .contact-lines svg {
    width: 8px;
    height: 8px;
    fill: var(--brand-blue);
  }
  .footer-bands {
    position: absolute;
    left: 0;
    bottom: 0;
    width: 664px;
    height: 56px;
    display: block;
  }
  .web-address {
    font-family: "Roboto", Arial, sans-serif;
    font-size: 10.5px;
    letter-spacing: 0.08em;
    fill: var(--white);
  }
</style>
</head>
<body>
  <main class="letterhead">
    <header>
      <div class="brand">
        <div class="brand-square" aria-hidden="true"></div>
        <p class="brand-name">Pennimartel<br>&amp; Pennimartel, LLP</p>
      </div>
      <div class="contact">
        <address>
          <span class="firm">Pennimartel &amp; Pennimartel, LLP</span><br>
          418 Harlow Street Suite 210<br>
          Alderbrook, New York 11850
        </address>
        <ul class="contact-lines">
          <li>
            <svg viewBox="0 0 10 10" aria-hidden="true"><path d="M2 0.5 L3.8 0.5 L4.4 3 L3.2 4 Q4.2 6 6 6.8 L7 5.6 L9.5 6.2 L9.5 8 Q9.5 9.5 8 9.5 Q1 9 0.5 2 Q0.5 0.5 2 0.5 Z"/></svg>
            (555) 410-2287
          </li>
          <li>
            <svg viewBox="0 0 10 10" aria-hidden="true"><rect x="2.5" y="0.5" width="5" height="3"/><rect x="0.5" y="4" width="9" height="4.5" rx="1"/></svg>
            (555) 410-2290
          </li>
          <li>
            <svg viewBox="0 0 10 10" aria-hidden="true"><path d="M0.5 2 H9.5 V8.5 H0.5 Z M1.5 3 V7.5 H8.5 V3 L5 5.6 Z"/></svg>
            info@pplawfirm.com
          </li>
        </ul>
      </div>
    </header>

    <svg class="footer-bands" viewBox="0 0 664 56" aria-hidden="false" role="presentation">
      <polygon points="0,28 452,28 440,40 0,40" fill="var(--brand-grey)"/>
      <polygon points="0,44 440,44 456,28 664,28 664,56 0,56" fill="var(--brand-blue)"/>
      <text class="web-address" x="640" y="46" text-anchor="end">www.pennimartellaw.com</text>
    </svg>
  </main>
</body>
</html>
```